Business Intelligence / Data Visualization Firm Seeking World Class Power Point Deck

Vane Crest delivers enterprise business intelligence and data visualization solutions enabling clients to see their business as they've never seen it - we transform complex, unstructured data into simple insight that facilitates intelligent decision making, revenue growth and risk reduction. We're seeking a world class power point template for internal, client and conference presentations.

Please visit vanecrest.com for more company context.
*Note: A website photo has been uploaded and may be used or not used - designer discretion.

Additional context:
We use Glimmerdash: https://glimmerdash.harvolo.com/products/predictive-analytics.

Target Market(s)

CXOs at Meridale 100 companies | small and medium business owners (BI / data-viz experts and also decision makers who don't actually understand BI / data-viz).

Industry/Entity Type

Professional Service

Font styles to use
Sans Serif
Other font styles liked:
• Our logo is Expansiva (uploaded), our site is Tahoma. Please use your discretion,.

Colors
ec1f27
ffffff
000000

Requirements
Must have
• PPT format, editable.
• Prefer simple, clean, strong presentation.
Nice to have
• Designs that relate to data, analytics, solutions, automation and transforming complexity into simplicity.
• Reusable icons.

```html
<!DOCTYPE html>
<html lang="en">
<head>
<meta charset="utf-8">
<title>Vane Crest – Presentation Template Overview</title>
<link rel="stylesheet" href="https://fonts.googleapis.com/css2?family=Montserrat:wght@500;600;700;800&family=Open+Sans:wght@400;600;700&display=swap">
<style>
:root{
  --red:#ec1f27;
  --dark:#3a3a3a;
  --darker:#2a2a2a;
  --ink:#222;
  --muted:#777;
  --line:#d9d9d9;
  --light:#e8e8e8;
  --white:#fff;
  --canvas:#959595;
  --photo-a:#5d6066;
  --photo-b:#2f3136;
}
*{box-sizing:border-box;margin:0;padding:0}
html,body{width:701px;height:1200px;overflow:hidden;background:var(--canvas)}
body{font-family:"Open Sans",Arial,sans-serif;color:var(--ink)}
.deck{display:grid;grid-template-columns:repeat(3,222px);grid-auto-rows:125px;column-gap:7.5px;row-gap:6px;padding:11px 10px}
.slide{position:relative;overflow:hidden;background:var(--white)}
.slide.dark{background:var(--dark);color:var(--white)}
.abs{position:absolute}
.photo{position:absolute;background:linear-gradient(135deg,var(--photo-a),var(--photo-b))}
.photo.light{background:linear-gradient(135deg,#b9b3ad,#6f6a66)}
.logo{font-family:"Montserrat",sans-serif;font-weight:600;letter-spacing:.18em;white-space:nowrap;display:inline-flex;align-items:center;gap:.35em}
.logo::before{content:"";width:.55em;height:.55em;border-radius:50%;background:var(--red)}
.title{font-family:"Montserrat",sans-serif;font-weight:800;line-height:1.1}
.t{font-size:3px;line-height:1.35;color:var(--muted)}
.dark .t,.t.inv{color:#cfcfcf}
.h{font-family:"Montserrat",sans-serif;font-weight:700;font-size:3.4px;color:var(--ink);line-height:1.3}
.dark .h,.h.inv{color:var(--white)}
.h.red{color:var(--red)}
.btn{display:inline-block;background:var(--red);color:var(--white);font-size:2.8px;font-weight:700;padding:1.4px 4px;border-radius:1px}
.hd{position:absolute;left:7px;top:6px;font-family:"Montserrat",sans-serif;font-weight:700;font-size:5px;color:var(--dark);border-left:1.4px solid var(--red);padding-left:2.5px;line-height:1.2}
.hd::before{content:"";position:absolute;left:-1.4px;top:-1px;width:8px;border-top:1.4px solid var(--red)}
.ft{position:absolute;left:6px;right:6px;bottom:4px;display:flex;align-items:center;gap:3px;font-size:2.3px;color:#999}
.ft .pg{background:var(--red);color:var(--white);width:5px;height:3.6px;display:flex;align-items:center;justify-content:center;font-size:2.2px}
.ft .logo{margin-left:auto;font-size:3px;color:var(--dark)}
.dark .ft .logo{color:var(--white)}
.ic{width:8px;height:8px;fill:none;stroke:currentColor;stroke-width:1.6}
.ring{border:0.6px solid var(--red);border-radius:50%;display:flex;align-items:center;justify-content:center;color:var(--red)}
table.data{border-collapse:collapse;width:100%;font-size:2.4px;color:#555}
table.data th{background:var(--red);color:var(--white);font-weight:700;padding:1.4px 1.5px;text-align:left}
table.data td{padding:1.5px;border-bottom:0.4px solid var(--line)}
table.data tr:nth-child(even) td{background:#f3f3f3}
table.data tfoot td{background:var(--dark);height:4px;padding:0}
.list{display:flex;flex-direction:column;gap:4px}
.item{display:flex;gap:2.5px;align-items:flex-start}
.dot{flex:none;width:6px;height:6px;border-radius:50%;background:var(--red);color:var(--white);display:flex;align-items:center;justify-content:center}
.dot.dk{background:var(--dark)}
.dot.gr{background:#888}
.dot .ic{width:4px;height:4px}
.row{display:flex}
</style>
</head>
<body>
<svg width="0" height="0" style="position:absolute">
  <defs>
    <symbol id="i-bars" viewBox="0 0 24 24"><path d="M4 20V11M10 20V5M16 20v-7M21 20H2"/></symbol>
    <symbol id="i-pie" viewBox="0 0 24 24"><circle cx="12" cy="12" r="8"/><path d="M12 4v8h8"/></symbol>
    <symbol id="i-target" viewBox="0 0 24 24"><circle cx="12" cy="12" r="8"/><circle cx="12" cy="12" r="3.5"/></symbol>
    <symbol id="i-doc" viewBox="0 0 24 24"><path d="M6 3h9l4 4v14H6z"/><path d="M9 11h7M9 15h7"/></symbol>
    <symbol id="i-clock" viewBox="0 0 24 24"><circle cx="12" cy="12" r="8"/><path d="M12 7v5l3 2"/></symbol>
    <symbol id="i-screen" viewBox="0 0 24 24"><rect x="3" y="4" width="18" height="12"/><path d="M9 20h6M12 16v4"/></symbol>
    <symbol id="i-pin" viewBox="0 0 24 24"><path d="M12 21s-6-6-6-11a6 6 0 0 1 12 0c0 5-6 11-6 11z"/><circle cx="12" cy="10" r="2"/></symbol>
    <symbol id="i-phone" viewBox="0 0 24 24"><path d="M6 3h4l2 5-3 2a11 11 0 0 0 5 5l2-3 5 2v4c0 1-1 2-2 2A17 17 0 0 1 4 5c0-1 1-2 2-2z"/></symbol>
    <symbol id="i-mail" viewBox="0 0 24 24"><rect x="3" y="6" width="18" height="12"/><path d="M3 6l9 7 9-7"/></symbol>
    <symbol id="i-globe" viewBox="0 0 24 24"><circle cx="12" cy="12" r="8"/><path d="M4 12h16M12 4c3 3 3 13 0 16M12 4c-3 3-3 13 0 16"/></symbol>
    <symbol id="i-bag" viewBox="0 0 24 24"><rect x="4" y="8" width="16" height="12"/><path d="M9 8V5h6v3"/></symbol>
  </defs>
</svg>

<main class="deck">

<!-- 1 Title dark -->
<section class="slide dark">
  <div class="photo light" style="left:70px;top:0;width:152px;height:82px" role="img" aria-label="Photo of a smiling business team"></div>
  <svg class="abs" style="left:0;top:0" width="222" height="125" viewBox="0 0 222 125">
    <polygon points="0,0 95,0 60,82 0,82" fill="#3a3a3a"/>
    <polygon points="95,0 104,0 66,82 60,82" fill="#ec1f27"/>
    <polygon points="0,0 38,0 0,30" fill="#ec1f27"/>
    <rect x="0" y="82" width="222" height="43" fill="#3a3a3a"/>
    <polygon points="150,125 222,60 222,125" fill="#ec1f27"/>
  </svg>
  <div class="abs" style="left:10px;top:78px;width:110px">
    <div class="logo" style="font-size:5px;color:#fff">VANE CREST</div>
    <div class="title" style="font-size:8.5px;margin-top:1px">POWERPOINT TITLE</div>
    <p class="t" style="margin:2px 0 3px">Lorem ipsum dolor sit amet, consectetuer adipiscing elit. Aenean commodo ligula eget dolor.</p>
    <span class="btn">Presented By: Mara Linden</span>
  </div>
</section>

<!-- 2 Title light -->
<section class="slide">
  <svg class="abs" style="left:0;top:0" width="222" height="125" viewBox="0 0 222 125" role="img" aria-label="Photo of hands typing on a laptop">
    <defs><linearGradient id="g2" x1="0" y1="0" x2="1" y2="1"><stop offset="0" stop-color="#c9b9a6"/><stop offset="1" stop-color="#5b4c40"/></linearGradient></defs>
    <path d="M128 0 C104 40 104 85 134 125 L222 125 L222 0Z" fill="#ec1f27"/>
    <path d="M137 0 C113 40 113 85 143 125 L222 125 L222 0Z" fill="url(#g2)"/>
  </svg>
  <div class="abs" style="left:10px;top:30px;width:100px">
    <div class="logo" style="font-size:5px;color:var(--ink)">VANE CREST</div>
    <div class="title" style="font-size:8.5px;margin-top:1px;color:var(--dark)">POWERPOINT TITLE</div>
    <p class="t" style="margin:2px 0 3px">Lorem ipsum dolor sit amet, consectetuer adipiscing elit. Aenean commodo ligula eget dolor. Aenean massa.</p>
    <span class="btn">Presented By: Mara Linden</span>
  </div>
</section>

<!-- 3 Title city -->
<section class="slide dark">
  <div class="photo" style="left:0;top:0;width:222px;height:70px;background:linear-gradient(180deg,#9aa0a6,#4a4e54)" role="img" aria-label="Photo of a city skyline"></div>
  <svg class="abs" style="left:0;top:0" width="222" height="125" viewBox="0 0 222 125">
    <polygon points="0,50 40,70 0,70" fill="#ec1f27"/>
    <polygon points="222,45 222,70 180,70" fill="#ec1f27"/>
  </svg>
  <div class="abs" style="left:0;right:0;top:76px;text-align:center">
    <div class="logo" style="font-size:5px;color:#fff">VANE CREST</div>
    <div class="title" style="font-size:8.5px;margin-top:1px">POWERPOINT TITLE</div>
    <p class="t" style="margin:2px auto 3px">Lorem ipsum dolor sit amet, consectetuer adipiscing elit. Aenean commodo ligula eget dolor. Aenean massa.</p>
    <span class="btn">Presented By: Mara Linden</span>
  </div>
</section>

<!-- 4 Content -->
<section class="slide">
  <div class="abs" style="left:8px;top:14px;width:88px;height:88px;border-radius:50%;border:0.6px dashed var(--red)"></div>
  <div class="abs" style="left:14px;top:20px;width:76px;height:76px;border-radius:50%;background:var(--dark);color:#fff;text-align:center;padding-top:26px">
    <div class="title" style="font-size:7.5px">CONTENT</div>
    <p class="t" style="width:46px;margin:2px auto 0">Lorem ipsum dolor sit amet, consectetuer adipiscing elit.</p>
  </div>
  <div class="abs dot" style="left:87px;top:52px;width:12px;height:12px;border:1px solid #fff"><svg class="ic" style="width:6px;height:6px"><use href="#i-bag"/></svg></div>
  <div class="abs" style="left:128px;top:18px;height:84px;border-left:0.6px solid var(--red)"></div>
  <div class="abs list" style="left:126px;top:16px;width:86px;gap:5px">
    <div class="item"><span class="dot" style="width:4px;height:4px;background:#fff;border:0.8px solid var(--red)"></span><div><div class="h">About Our Company</div><p class="t">Lorem ipsum dolor sit amet, consec adipiscing elit.</p></div></div>
    <div class="item"><span class="dot" style="width:4px;height:4px;background:#fff;border:0.8px solid var(--red)"></span><div><div class="h">What We Do</div><p class="t">Lorem ipsum dolor sit amet, consec adipiscing elit.</p></div></div>
    <div class="item"><span class="dot" style="width:4px;height:4px;background:#fff;border:0.8px solid var(--red)"></span><div><div class="h">Our Service</div><p class="t">Lorem ipsum dolor sit amet, consec adipiscing elit.</p></div></div>
    <div class="item"><span class="dot" style="width:4px;height:4px;background:#fff;border:0.8px solid var(--red)"></span><div><div class="h">Our Value</div><p class="t">Lorem ipsum dolor sit amet, consec adipiscing elit.</p></div></div>
    <div class="item"><span class="dot" style="width:4px;height:4px;background:#fff;border:0.8px solid var(--red)"></span><div><div class="h">Contact Us</div><p class="t">Lorem ipsum dolor sit amet, consec adipiscing elit.</p></div></div>
  </div>
  <div class="ft"><span class="pg">4</span>Copyright © 2017 Vane Crest | All Rights Reserved<span class="logo">VANE CREST</span></div>
</section>

<!-- 5 About -->
<section class="slide">
  <div class="photo" style="left:0;top:0;width:222px;height:48px;background:linear-gradient(180deg,#d5d5d5,#a9a9a9)" role="img" aria-label="Soft photo of an office desk"></div>
  <div class="abs" style="left:58px;top:16px;width:106px;height:26px;background:var(--dark);border-radius:0 0 4px 4px;display:flex;align-items:center;justify-content:center">
    <span class="logo" style="font-size:8px;color:#fff;font-weight:500">VANE CREST</span>
  </div>
  <div class="abs" style="left:14px;right:14px;top:58px;text-align:center">
    <div class="h" style="font-size:4px">About Our Company</div>
    <p class="t" style="margin-top:2px">Lorem ipsum dolor sit amet, consectetuer adipiscing elit. Aenean commodo ligula eget dolor. Aenean massa. Cum sociis natoque penatibus et magnis dis parturient montes, nascetur ridiculus mus. Donec quam felis, ultricies nec, pellentesque eu, pretium quis, sem.</p>
    <p class="t" style="margin-top:2px">Aliquam lorem ante, dapibus in, viverra quis, feugiat a, tellus. Phasellus viverra nulla ut metus varius laoreet. Quisque rutrum. Aenean imperdiet. Etiam ultricies nisi vel augue. Curabitur ullamcorper ultricies nisi.</p>
  </div>
  <div class="ft"><span class="pg">5</span>Copyright © 2017 Vane Crest | All Rights Reserved<span class="logo">VANE CREST</span></div>
</section>

<!-- 6 Intro red box -->
<section class="slide">
  <div class="photo" style="left:0;top:0;width:222px;height:40px" role="img" aria-label="Dark photo of city buildings"></div>
  <div class="abs" style="left:8px;top:8px;width:72px;height:92px;background:var(--red);color:#fff;padding:14px 6px 0;clip-path:polygon(0 0,100% 0,100% 100%,10px 100%,0 calc(100% - 10px))">
    <div class="title" style="font-size:5.2px">Write Something About Your Title or Topic Here</div>
    <p class="t inv" style="margin-top:3px">Lorem ipsum dolor sit amet, consectetuer adipiscing elit. Aenean commodo ligula eget dolor. Aenean massa. Cum sociis natoque penatibus et magnis dis parturient montes.</p>
  </div>
  <div class="abs" style="left:90px;top:10px;width:124px">
    <div class="h inv" style="font-size:4px">Vane Crest Powerpoint</div>
    <p class="t inv" style="margin-top:1px">Lorem ipsum dolor sit amet, consectetuer adipiscing elit. Aenean commodo ligula eget dolor. Aenean massa. Cum sociis natoque.</p>
  </div>
  <div class="abs row" style="left:94px;top:54px;width:120px;justify-content:space-between;text-align:center">
    <div style="width:36px"><div class="ring" style="width:11px;height:11px;margin:0 auto 3px"><svg class="ic" style="width:6px;height:6px"><use href="#i-target"/></svg></div><div class="h">Insert Text Here</div><p class="t">Lorem ipsum dolor sit amet, consec</p></div>
    <div style="width:36px"><div class="ring" style="width:11px;height:11px;margin:0 auto 3px"><svg class="ic" style="width:6px;height:6px"><use href="#i-clock"/></svg></div><div class="h">Insert Text Here</div><p class="t">Lorem ipsum dolor sit amet, consec</p></div>
    <div style="width:36px"><div class="ring" style="width:11px;height:11px;margin:0 auto 3px"><svg class="ic" style="width:6px;height:6px"><use href="#i-pie"/></svg></div><div class="h">Insert Text Here</div><p class="t">Lorem ipsum dolor sit amet, consec</p></div>
  </div>
  <div class="ft"><span class="pg">6</span>Copyright © 2017 Vane Crest | All Rights Reserved<span class="logo">VANE CREST</span></div>
</section>

<!-- 7 Dark band + 4 items -->
<section class="slide">
  <div class="hd">Vane Crest Powerpoint Template</div>
  <div class="abs" style="left:0;top:20px;width:222px;height:40px;background:var(--dark);display:flex;gap:8px;padding:8px 8px 0">
    <div class="title" style="font-size:5.2px;color:#fff;width:70px">Write Something About Your Title or Topic Here</div>
    <p class="t inv" style="flex:1">Lorem ipsum dolor sit amet, consectetuer adipiscing elit. Aenean commodo ligula eget dolor. Aenean massa. Cum sociis natoque penatibus et magnis dis parturient montes, nascetur ridiculus mus. Donec quam felis, ultricies nec.</p>
  </div>
  <div class="abs" style="left:8px;top:68px;width:206px;display:grid;grid-template-columns:1fr 1fr;gap:6px 10px">
    <div class="item"><span class="dot" style="border-radius:1px"><svg class="ic"><use href="#i-bars"/></svg></span><div><div class="h">Insert text here</div><p class="t">Lorem ipsum dolor sit amet, consectetuer adipiscing elit. Aenean commodo.</p></div></div>
    <div class="item"><span class="dot" style="border-radius:1px"><svg class="ic"><use href="#i-doc"/></svg></span><div><div class="h">Insert text here</div><p class="t">Lorem ipsum dolor sit amet, consectetuer adipiscing elit. Aenean commodo.</p></div></div>
    <div class="item"><span class="dot" style="border-radius:1px"><svg class="ic"><use href="#i-screen"/></svg></span><div><div class="h">Insert text here</div><p class="t">Lorem ipsum dolor sit amet, consectetuer adipiscing elit. Aenean commodo.</p></div></div>
    <div class="item"><span class="dot" style="border-radius:1px"><svg class="ic"><use href="#i-pie"/></svg></span><div><div class="h">Insert text here</div><p class="t">Lorem ipsum dolor sit amet, consectetuer adipiscing elit. Aenean commodo.</p></div></div>
  </div>
  <div class="ft"><span class="pg">7</span>Copyright © 2017 Vane Crest | All Rights Reserved<span class="logo">VANE CREST</span></div>
</section>

<!-- 8 Numbered boxes -->
<section class="slide">
  <div class="hd">Vane Crest Powerpoint Template</div>
  <div class="abs" style="left:8px;top:20px;width:206px;display:grid;grid-template-columns:1fr 1fr;gap:5px 8px">
    <div class="row" style="height:25px"><div style="width:14px;background:var(--red);color:#fff;font:800 13px Montserrat,sans-serif;display:flex;align-items:center;justify-content:center">1</div><div style="flex:1;background:var(--dark);padding:3px"><div class="h inv">Insert text here</div><p class="t inv">Lorem ipsum dolor sit amet, consectetuer adipiscing elit. Aenean commodo.</p></div></div>
    <div class="row" style="height:25px"><div style="width:14px;background:var(--red);color:#fff;font:800 13px Montserrat,sans-serif;display:flex;align-items:center;justify-content:center">4</div><div style="flex:1;background:var(--dark);padding:3px"><div class="h inv">Insert text here</div><p class="t inv">Lorem ipsum dolor sit amet, consectetuer adipiscing elit. Aenean commodo.</p></div></div>
    <div class="row" style="height:25px"><div style="width:14px;background:var(--red);color:#fff;font:800 13px Montserrat,sans-serif;display:flex;align-items:center;justify-content:center">2</div><div style="flex:1;background:var(--dark);padding:3px"><div class="h inv">Insert text here</div><p class="t inv">Lorem ipsum dolor sit amet, consectetuer adipiscing elit. Aenean commodo.</p></div></div>
    <div class="row" style="height:25px"><div style="width:14px;background:var(--red);color:#fff;font:800 13px Montserrat,sans-serif;display:flex;align-items:center;justify-content:center">5</div><div style="flex:1;background:var(--dark);padding:3px"><div class="h inv">Insert text here</div><p class="t inv">Lorem ipsum dolor sit amet, consectetuer adipiscing elit. Aenean commodo.</p></div></div>
    <div class="row" style="height:25px"><div style="width:14px;background:var(--red);color:#fff;font:800 13px Montserrat,sans-serif;display:flex;align-items:center;justify-content:center">3</div><div style="flex:1;background:var(--dark);padding:3px"><div class="h inv">Insert text here</div><p class="t inv">Lorem ipsum dolor sit amet, consectetuer adipiscing elit. Aenean commodo.</p></div></div>
    <div class="row" style="height:25px"><div style="width:14px;background:var(--red);color:#fff;font:800 13px Montserrat,sans-serif;display:flex;align-items:center;justify-content:center">6</div><div style="flex:1;background:var(--dark);padding:3px"><div class="h inv">Insert text here</div><p class="t inv">Lorem ipsum dolor sit amet, consectetuer adipiscing elit. Aenean commodo.</p></div></div>
  </div>
  <div class="ft"><span class="pg">8</span>Copyright © 2017 Vane Crest | All Rights Reserved<span class="logo">VANE CREST</span></div>
</section>

<!-- 9 Red icon tiles -->
<section class="slide">
  <div class="hd">Vane Crest Powerpoint Template</div>
  <div class="abs row" style="left:8px;top:28px;width:206px;gap:6px">
    <div style="flex:1"><div style="background:var(--red);height:34px;color:#fff;text-align:center;padding-top:8px"><svg class="ic" style="width:12px;height:12px;stroke-width:1.3"><use href="#i-screen"/></svg><div class="h inv" style="margin-top:2px">Insert text here</div></div><div style="background:var(--dark);height:28px;padding:4px;text-align:center"><p class="t inv">Lorem ipsum dolor sit amet, consectetuer adipiscing elit. Aenean commodo.</p></div></div>
    <div style="flex:1"><div style="background:var(--red);height:34px;color:#fff;text-align:center;padding-top:8px"><svg class="ic" style="width:12px;height:12px;stroke-width:1.3"><use href="#i-bars"/></svg><div class="h inv" style="margin-top:2px">Insert text here</div></div><div style="background:var(--dark);height:28px;padding:4px;text-align:center"><p class="t inv">Lorem ipsum dolor sit amet, consectetuer adipiscing elit. Aenean commodo.</p></div></div>
    <div style="flex:1"><div style="background:var(--red);height:34px;color:#fff;text-align:center;padding-top:8px"><svg class="ic" style="width:12px;height:12px;stroke-width:1.3"><use href="#i-clock"/></svg><div class="h inv" style="margin-top:2px">Insert text here</div></div><div style="background:var(--dark);height:28px;padding:4px;text-align:center"><p class="t inv">Lorem ipsum dolor sit amet, consectetuer adipiscing elit. Aenean commodo.</p></div></div>
    <div style="flex:1"><div style="background:var(--red);height:34px;color:#fff;text-align:center;padding-top:8px"><svg class="ic" style="width:12px;height:12px;stroke-width:1.3"><use href="#i-doc"/></svg><div class="h inv" style="margin-top:2px">Insert text here</div></div><div style="background:var(--dark);height:28px;padding:4px;text-align:center"><p class="t inv">Lorem ipsum dolor sit amet, consectetuer adipiscing elit. Aenean commodo.</p></div></div>
  </div>
  <div class="ft"><span class="pg">9</span>Copyright © 2017 Vane Crest | All Rights Reserved<span class="logo">VANE CREST</span></div>
</section>

<!-- 10 Arrow timeline -->
<section class="slide">
  <div class="hd">Vane Crest Powerpoint Template</div>
  <svg class="abs" style="left:0;top:0" width="222" height="125" viewBox="0 0 222 125">
    <polygon points="8,55 50,55 56,61 50,67 8,67 14,61" fill="#ec1f27"/>
    <polygon points="52,55 102,55 108,61 102,67 52,67 58,61" fill="#3a3a3a"/>
    <polygon points="104,55 154,55 160,61 154,67 104,67 110,61" fill="#ec1f27"/>
    <polygon points="156,55 208,55 214,61 208,67 156,67 162,61" fill="#3a3a3a"/>
    <line x1="40" y1="46" x2="40" y2="55" stroke="#3a3a3a" stroke-width=".6"/>
    <line x1="134" y1="46" x2="134" y2="55" stroke="#3a3a3a" stroke-width=".6"/>
    <line x1="86" y1="67" x2="86" y2="74" stroke="#ec1f27" stroke-width=".6"/>
    <line x1="182" y1="67" x2="182" y2="74" stroke="#ec1f27" stroke-width=".6"/>
    <circle cx="40" cy="40" r="6" fill="#3a3a3a"/><circle cx="134" cy="40" r="6" fill="#3a3a3a"/>
    <circle cx="86" cy="80" r="6" fill="#ec1f27"/><circle cx="182" cy="80" r="6" fill="#ec1f27"/>
  </svg>
  <div class="abs" style="left:80px;top:36px;width:40px"><div class="h">Insert Text Here</div><p class="t">Lorem ipsum dolor sit amet, consectetuer</p></div>
  <div class="abs" style="left:174px;top:36px;width:40px"><div class="h">Insert Text Here</div><p class="t">Lorem ipsum dolor sit amet, consectetuer</p></div>
  <div class="abs" style="left:22px;top:76px;width:40px"><div class="h">Insert Text Here</div><p class="t">Lorem ipsum dolor sit amet, consectetuer</p></div>
  <div class="abs" style="left:116px;top:76px;width:40px"><div class="h">Insert Text Here</div><p class="t">Lorem ipsum dolor sit amet, consectetuer</p></div>
  <div class="ft"><span class="pg">10</span>Copyright © 2017 Vane Crest | All Rights Reserved<span class="logo">VANE CREST</span></div>
</section>

<!-- 11 Circle chain -->
<section class="slide">
  <div class="hd">Vane Crest Powerpoint Template</div>
  <svg class="abs" style="left:0;top:0" width="222" height="125" viewBox="0 0 222 125">
    <path d="M40 62 Q62 40 84 62 T128 62 T172 62" fill="none" stroke="#ec1f27" stroke-width="8"/>
    <path d="M18 62 Q40 84 62 62 T106 62 T150 62 T194 62" fill="none" stroke="#3a3a3a" stroke-width="8"/>
    <g fill="#fff" stroke="#3a3a3a" stroke-width="1.4">
      <circle cx="62" cy="50" r="9"/><circle cx="106" cy="50" r="9"/><circle cx="150" cy="50" r="9"/><circle cx="194" cy="50" r="9" stroke="#ec1f27"/>
    </g>
    <g fill="#fff" stroke="#ec1f27" stroke-width="1.4">
      <circle cx="40" cy="76" r="9"/><circle cx="84" cy="76" r="9"/><circle cx="128" cy="76" r="9"/><circle cx="172" cy="76" r="9" stroke="#3a3a3a"/>
    </g>
    <g fill="#ec1f27"><circle cx="62" cy="50" r="2.5"/><circle cx="106" cy="50" r="2.5"/><circle cx="150" cy="50" r="2.5"/><circle cx="194" cy="50" r="2.5"/></g>
    <g fill="#3a3a3a"><circle cx="40" cy="76" r="2.5"/><circle cx="84" cy="76" r="2.5"/><circle cx="128" cy="76" r="2.5"/><circle cx="172" cy="76" r="2.5"/></g>
  </svg>
  <div class="abs row" style="left:44px;top:22px;width:168px;justify-content:space-between;text-align:center">
    <div style="width:36px"><div class="h">Insert Text Here</div><p class="t">Lorem ipsum dolor sit amet</p></div>
    <div style="width:36px"><div class="h">Insert Text Here</div><p class="t">Lorem ipsum dolor sit amet</p></div>
    <div style="width:36px"><div class="h">Insert Text Here</div><p class="t">Lorem ipsum dolor sit amet</p></div>
    <div style="width:36px"><div class="h">Insert Text Here</div><p class="t">Lorem ipsum dolor sit amet</p></div>
  </div>
  <div class="abs row" style="left:22px;top:90px;width:168px;justify-content:space-between;text-align:center">
    <div style="width:36px"><div class="h">Insert Text Here</div><p class="t">Lorem ipsum dolor sit amet</p></div>
    <div style="width:36px"><div class="h">Insert Text Here</div><p class="t">Lorem ipsum dolor sit amet</p></div>
    <div style="width:36px"><div class="h">Insert Text Here</div><p class="t">Lorem ipsum dolor sit amet</p></div>
    <div style="width:36px"><div class="h">Insert Text Here</div><p class="t">Lorem ipsum dolor sit amet</p></div>
  </div>
  <div class="ft"><span class="pg">11</span>Copyright © 2017 Vane Crest | All Rights Reserved<span class="logo">VANE CREST</span></div>
</section>

<!-- 12 Text + red bar list -->
<section class="slide">
  <div class="abs" style="left:10px;top:28px;width:100px">
    <div class="title" style="font-size:5.8px;color:var(--dark);border-left:1.4px solid var(--red);padding-left:3px">Write Something About Your Title or Topic Here</div>
    <p class="t" style="margin-top:4px">Lorem ipsum dolor sit amet, consectetuer adipiscing elit. Aenean commodo ligula eget dolor. Aenean massa. Cum sociis natoque penatibus et magnis dis parturient montes.</p>
    <p class="t" style="margin-top:2px">Aliquam lorem ante, dapibus in, viverra quis, feugiat a, tellus. Phasellus viverra nulla ut metus varius laoreet. Quisque rutrum. Aenean imperdiet. Etiam ultricies nisi vel augue.</p>
  </div>
  <div class="abs" style="left:118px;top:10px;width:14px;height:102px;background:var(--red);display:flex;flex-direction:column;justify-content:space-around;align-items:center;color:#fff">
    <svg class="ic"><use href="#i-bars"/></svg><svg class="ic"><use href="#i-screen"/></svg><svg class="ic"><use href="#i-pie"/></svg><svg class="ic"><use href="#i-doc"/></svg>
  </div>
  <div class="abs" style="left:138px;top:12px;width:76px;display:flex;flex-direction:column;gap:8px">
    <div><div class="h">Insert Text Here</div><p class="t">Lorem ipsum dolor sit amet, consectetuer adipiscing elit. Aenean commodo ligula.</p></div>
    <div><div class="h">Insert Text Here</div><p class="t">Lorem ipsum dolor sit amet, consectetuer adipiscing elit. Aenean commodo ligula.</p></div>
    <div><div class="h">Insert Text Here</div><p class="t">Lorem ipsum dolor sit amet, consectetuer adipiscing elit. Aenean commodo ligula.</p></div>
    <div><div class="h">Insert Text Here</div><p class="t">Lorem ipsum dolor sit amet, consectetuer adipiscing elit. Aenean commodo ligula.</p></div>
  </div>
  <div class="ft"><span class="pg">12</span>Copyright © 2017 Vane Crest | All Rights Reserved<span class="logo">VANE CREST</span></div>
</section>

<!-- 13 Grouped bars -->
<section class="slide">
  <div class="hd">Vane Crest Powerpoint Template</div>
  <svg class="abs" style="left:6px;top:24px" width="110" height="84" viewBox="0 0 110 84" role="img" aria-label="Grouped bar chart for January to March">
    <g font-size="2.6" fill="#999" font-family="Open Sans,sans-serif">
      <text x="0" y="4">40</text><text x="0" y="20">30</text><text x="0" y="36">20</text><text x="0" y="52">10</text><text x="2" y="68">0</text>
      <text x="18" y="76">January</text><text x="52" y="76">February</text><text x="86" y="76">March</text>
    </g>
    <g stroke="#eee" stroke-width=".4"><line x1="8" y1="3" x2="108" y2="3"/><line x1="8" y1="19" x2="108" y2="19"/><line x1="8" y1="35" x2="108" y2="35"/><line x1="8" y1="51" x2="108" y2="51"/><line x1="8" y1="67" x2="108" y2="67"/></g>
    <rect x="14" y="15" width="7" height="52" fill="#3a3a3a"/><rect x="22" y="7" width="7" height="60" fill="#ec1f27"/><rect x="30" y="31" width="7" height="36" fill="#ddd"/>
    <rect x="48" y="7" width="7" height="60" fill="#3a3a3a"/><rect x="56" y="27" width="7" height="40" fill="#ec1f27"/><rect x="64" y="47" width="7" height="20" fill="#ddd"/>
    <rect x="82" y="11" width="7" height="56" fill="#3a3a3a"/><rect x="90" y="35" width="7" height="32" fill="#ec1f27"/><rect x="98" y="47" width="7" height="20" fill="#ddd"/>
  </svg>
  <div class="abs list" style="left:128px;top:36px;width:88px;gap:7px">
    <div class="item"><span class="ring" style="width:7px;height:7px;flex:none"><svg class="ic" style="width:4px;height:4px"><use href="#i-bars"/></svg></span><div><div class="h">Insert Text Here</div><p class="t">Lorem ipsum dolor sit amet, consectetuer adipiscing elit. Aenean commodo.</p></div></div>
    <div class="item"><span class="ring" style="width:7px;height:7px;flex:none"><svg class="ic" style="width:4px;height:4px"><use href="#i-clock"/></svg></span><div><div class="h">Insert Text Here</div><p class="t">Lorem ipsum dolor sit amet, consectetuer adipiscing elit. Aenean commodo.</p></div></div>
    <div class="item"><span class="ring" style="width:7px;height:7px;flex:none"><svg class="ic" style="width:4px;height:4px"><use href="#i-doc"/></svg></span><div><div class="h">Insert Text Here</div><p class="t">Lorem ipsum dolor sit amet, consectetuer adipiscing elit. Aenean commodo.</p></div></div>
  </div>
  <div class="ft"><span class="pg">13</span>Copyright © 2017 Vane Crest | All Rights Reserved<span class="logo">VANE CREST</span></div>
</section>

<!-- 14 Monthly bars -->
<section class="slide">
  <div class="hd">Vane Crest Powerpoint Template</div>
  <svg class="abs" style="left:12px;top:22px" width="198" height="62" viewBox="0 0 198 62" role="img" aria-label="Bar chart rising from January to December">
    <g font-size="2.4" fill="#fff" font-family="Open Sans,sans-serif" text-anchor="middle">
      <rect x="4" y="44" width="9" height="6" fill="#d4d4d4"/><rect x="20" y="40" width="9" height="10" fill="#c4c4c4"/><rect x="36" y="35" width="9" height="15" fill="#b4b4b4"/><rect x="52" y="32" width="9" height="18" fill="#a4a4a4"/><rect x="68" y="28" width="9" height="22" fill="#8a8a8a"/><rect x="84" y="25" width="9" height="25" fill="#6f6f6f"/><rect x="100" y="20" width="9" height="30" fill="#4d4d4d"/><rect x="116" y="16" width="9" height="34" fill="#3a3a3a"/><rect x="132" y="13" width="9" height="37" fill="#2e2e2e"/><rect x="148" y="9" width="9" height="41" fill="#ec1f27"/><rect x="164" y="5" width="9" height="45" fill="#ec1f27"/><rect x="180" y="2" width="9" height="48" fill="#ec1f27"/>
      <text x="8.5" y="48">1</text><text x="24.5" y="46">2</text><text x="40.5" y="44">3</text><text x="56.5" y="42">4</text><text x="72.5" y="40">5</text><text x="88.5" y="38">6</text><text x="104.5" y="36">7</text><text x="120.5" y="34">8</text><text x="136.5" y="32">9</text><text x="152.5" y="30">10</text><text x="168.5" y="28">11</text><text x="184.5" y="26">12</text>
    </g>
    <g font-size="2.4" fill="#888" font-family="Open Sans,sans-serif" text-anchor="middle">
      <text x="8.5" y="56">Jan</text><text x="24.5" y="56">Feb</text><text x="40.5" y="56">Mar</text><text x="56.5" y="56">Apr</text><text x="72.5" y="56">May</text><text x="88.5" y="56">Jun</text><text x="104.5" y="56">Jul</text><text x="120.5" y="56">Aug</text><text x="136.5" y="56">Sep</text><text x="152.5" y="56">Oct</text><text x="168.5" y="56">Nov</text><text x="184.5" y="56">Dec</text>
    </g>
  </svg>
  <p class="t abs" style="left:20px;right:20px;top:88px;text-align:center">Lorem ipsum dolor sit amet, consectetuer adipiscing elit. Aenean commodo ligula eget dolor. Aenean massa. Cum sociis natoque penatibus et magnis dis parturient montes, nascetur ridiculus mus. Donec quam felis, ultricies nec, pellentesque eu, pretium quis, sem.</p>
  <div class="ft"><span class="pg">14</span>Copyright © 2017 Vane Crest | All Rights Reserved<span class="logo">VANE CREST</span></div>
</section>

<!-- 15 Donuts -->
<section class="slide">
  <div class="hd">Vane Crest Powerpoint Template</div>
  <div class="abs row" style="left:8px;top:32px;width:206px;justify-content:space-between;text-align:center">
    <div style="width:46px"><svg width="34" height="34" viewBox="0 0 34 34"><circle cx="17" cy="17" r="14" fill="none" stroke="#3a3a3a" stroke-width="3.5"/><circle cx="17" cy="17" r="14" fill="none" stroke="#ec1f27" stroke-width="3.5" stroke-dasharray="74.8 88" transform="rotate(-90 17 17)"/><text x="17" y="19.3" text-anchor="middle" font-size="6.5" font-weight="700" font-family="Montserrat,sans-serif" fill="#3a3a3a">85%</text></svg><div class="h" style="margin-top:3px">Market Data</div><p class="t">Lorem ipsum dolor sit amet, consectetuer adipiscing elit. Aenean commodo.</p></div>
    <div style="width:46px"><svg width="34" height="34" viewBox="0 0 34 34"><circle cx="17" cy="17" r="14" fill="none" stroke="#3a3a3a" stroke-width="3.5"/><circle cx="17" cy="17" r="14" fill="none" stroke="#ec1f27" stroke-width="3.5" stroke-dasharray="59.8 88" transform="rotate(-90 17 17)"/><text x="17" y="19.3" text-anchor="middle" font-size="6.5" font-weight="700" font-family="Montserrat,sans-serif" fill="#3a3a3a">68%</text></svg><div class="h" style="margin-top:3px">Market Data</div><p class="t">Lorem ipsum dolor sit amet, consectetuer adipiscing elit. Aenean commodo.</p></div>
    <div style="width:46px"><svg width="34" height="34" viewBox="0 0 34 34"><circle cx="17" cy="17" r="14" fill="none" stroke="#3a3a3a" stroke-width="3.5"/><circle cx="17" cy="17" r="14" fill="none" stroke="#ec1f27" stroke-width="3.5" stroke-dasharray="39.6 88" transform="rotate(-90 17 17)"/><text x="17" y="19.3" text-anchor="middle" font-size="6.5" font-weight="700" font-family="Montserrat,sans-serif" fill="#3a3a3a">45%</text></svg><div class="h" style="margin-top:3px">Market Data</div><p class="t">Lorem ipsum dolor sit amet, consectetuer adipiscing elit. Aenean commodo.</p></div>
    <div style="width:46px"><svg width="34" height="34" viewBox="0 0 34 34"><circle cx="17" cy="17" r="14" fill="none" stroke="#3a3a3a" stroke-width="3.5"/><circle cx="17" cy="17" r="14" fill="none" stroke="#ec1f27" stroke-width="3.5" stroke-dasharray="65.1 88" transform="rotate(-90 17 17)"/><text x="17" y="19.3" text-anchor="middle" font-size="6.5" font-weight="700" font-family="Montserrat,sans-serif" fill="#3a3a3a">74%</text></svg><div class="h" style="margin-top:3px">Market Data</div><p class="t">Lorem ipsum dolor sit amet, consectetuer adipiscing elit. Aenean commodo.</p></div>
  </div>
  <div class="ft"><span class="pg">15</span>Copyright © 2017 Vane Crest | All Rights Reserved<span class="logo">VANE CREST</span></div>
</section>

<!-- 16 Full table -->
<section class="slide">
  <div class="hd">Vane Crest Powerpoint Template</div>
  <div class="abs" style="left:8px;top:22px;width:206px">
    <table class="data">
      <thead><tr><th>Item Description</th><th>Number</th><th>Number</th><th>Text Title</th><th>Text Title</th></tr></thead>
      <tbody>
        <tr><td>Lorem ipsum</td><td>4.3</td><td>4.2</td><td>Important Data Analysis</td><td>Yes</td></tr>
        <tr><td>Lorem ipsum</td><td>4.1</td><td>4.4</td><td>Important Data Analysis</td><td>No</td></tr>
        <tr><td>Lorem ipsum</td><td>3.3</td><td>3.5</td><td>Important Data Analysis</td><td>Yes</td></tr>
        <tr><td>Lorem ipsum</td><td>2.1</td><td>2.8</td><td>Important Data Analysis</td><td>Yes</td></tr>
        <tr><td>Lorem ipsum</td><td>1.7</td><td>1.5</td><td>Important Data Analysis</td><td>Yes</td></tr>
      </tbody>
      <tfoot><tr><td colspan="5"></td></tr></tfoot>
    </table>
    <p class="t" style="margin-top:5px;text-align:center">Lorem ipsum dolor sit amet, consectetuer adipiscing elit. Aenean commodo ligula eget dolor. Aenean massa. Cum sociis natoque penatibus et magnis dis parturient montes, nascetur ridiculus mus. Donec quam felis, ultricies nec.</p>
  </div>
  <div class="ft"><span class="pg">16</span>Copyright © 2017 Vane Crest | All Rights Reserved<span class="logo">VANE CREST</span></div>
</section>

<!-- 17 Two tables -->
<section class="slide">
  <div class="hd">Vane Crest Powerpoint Template</div>
  <div class="abs row" style="left:8px;top:22px;width:206px;gap:8px">
    <div style="flex:1">
      <table class="data"><thead><tr><th>Item Description</th><th>Number</th><th>Text Title</th><th>Text Title</th></tr></thead>
        <tbody><tr><td>Lorem ipsum</td><td>4.3</td><td>Data Analysis</td><td>Yes</td></tr><tr><td>Lorem ipsum</td><td>4.1</td><td>Data Analysis</td><td>No</td></tr><tr><td>Lorem ipsum</td><td>3.3</td><td>Data Analysis</td><td>Yes</td></tr><tr><td>Lorem ipsum</td><td>2.1</td><td>Data Analysis</td><td>Yes</td></tr><tr><td>Lorem ipsum</td><td>1.7</td><td>Data Analysis</td><td>Yes</td></tr></tbody>
        <tfoot><tr><td colspan="4"></td></tr></tfoot></table>
      <div class="h" style="margin-top:5px">Insert Text Here</div><p class="t">Lorem ipsum dolor sit amet, consectetuer adipiscing elit. Aenean commodo ligula eget dolor. Aenean massa.</p>
    </div>
    <div style="flex:1">
      <table class="data"><thead><tr><th>Item Description</th><th>Number</th><th>Text Title</th><th>Text Title</th></tr></thead>
        <tbody><tr><td>Lorem ipsum</td><td>4.3</td><td>Data Analysis</td><td>Yes</td></tr><tr><td>Lorem ipsum</td><td>4.1</td><td>Data Analysis</td><td>No</td></tr><tr><td>Lorem ipsum</td><td>3.3</td><td>Data Analysis</td><td>Yes</td></tr><tr><td>Lorem ipsum</td><td>2.1</td><td>Data Analysis</td><td>Yes</td></tr><tr><td>Lorem ipsum</td><td>1.7</td><td>Data Analysis</td><td>Yes</td></tr></tbody>
        <tfoot><tr><td colspan="4"></td></tr></tfoot></table>
      <div class="h" style="margin-top:5px">Insert Text Here</div><p class="t">Lorem ipsum dolor sit amet, consectetuer adipiscing elit. Aenean commodo ligula eget dolor. Aenean massa.</p>
    </div>
  </div>
  <div class="ft"><span class="pg">17</span>Copyright © 2017 Vane Crest | All Rights Reserved<span class="logo">VANE CREST</span></div>
</section>

<!-- 18 Table + text -->
<section class="slide">
  <div class="hd">Vane Crest Powerpoint Template</div>
  <div class="abs" style="left:8px;top:22px;width:110px">
    <table class="data" style="font-size:2.3px"><thead><tr><th>Item Description</th><th>Number</th><th>Text Title</th><th>Text Title</th></tr></thead>
      <tbody><tr><td style="padding:3px 1.5px">Lorem ipsum</td><td>4.3</td><td>Data Analysis</td><td>Yes</td></tr><tr><td style="padding:3px 1.5px">Lorem ipsum</td><td>4.1</td><td>Data Analysis</td><td>No</td></tr><tr><td style="padding:3px 1.5px">Lorem ipsum</td><td>3.3</td><td>Data Analysis</td><td>Yes</td></tr><tr><td style="padding:3px 1.5px">Lorem ipsum</td><td>2.1</td><td>Data Analysis</td><td>No</td></tr><tr><td style="padding:3px 1.5px">Lorem ipsum</td><td>1.7</td><td>Data Analysis</td><td>Yes</td></tr></tbody>
      <tfoot><tr><td colspan="4"></td></tr></tfoot></table>
  </div>
  <div class="abs" style="left:126px;top:22px;width:88px">
    <div class="title" style="font-size:4.6px;color:var(--dark)">Write Something About Your Title or Topic Here</div>
    <p class="t" style="margin:2px 0 4px">Lorem ipsum dolor sit amet, consectetuer adipiscing elit. Aenean commodo ligula eget dolor.</p>
    <div class="list" style="gap:3px">
      <div class="item"><span class="dot"><svg class="ic"><use href="#i-pie"/></svg></span><div><div class="h">Insert Text Here</div><p class="t">Lorem ipsum dolor sit amet, consectetuer adipiscing elit.</p></div></div>
      <div class="item"><span class="dot dk"><svg class="ic"><use href="#i-clock"/></svg></span><div><div class="h">Insert Text Here</div><p class="t">Lorem ipsum dolor sit amet, consectetuer adipiscing elit.</p></div></div>
      <div class="item"><span class="dot gr"><svg class="ic"><use href="#i-target"/></svg></span><div><div class="h">Insert Text Here</div><p class="t">Lorem ipsum dolor sit amet, consectetuer adipiscing elit.</p></div></div>
    </div>
  </div>
  <div class="ft"><span class="pg">18</span>Copyright © 2017 Vane Crest | All Rights Reserved<span class="logo">VANE CREST</span></div>
</section>

<!-- 19 Six icon items -->
<section class="slide">
  <div class="hd">Vane Crest Powerpoint Template</div>
  <div class="abs" style="left:14px;top:22px;width:194px;display:grid;grid-template-columns:repeat(3,1fr);gap:8px 14px;text-align:center;color:var(--red)">
    <div><svg class="ic" style="width:9px;height:9px;stroke-width:1.2"><use href="#i-bag"/></svg><div class="h">Insert Text Here</div><p class="t">Lorem ipsum dolor sit amet, consectetuer adipiscing elit. Aenean commodo ligula eget dolor.</p></div>
    <div><svg class="ic" style="width:9px;height:9px;stroke-width:1.2"><use href="#i-globe"/></svg><div class="h">Insert Text Here</div><p class="t">Lorem ipsum dolor sit amet, consectetuer adipiscing elit. Aenean commodo ligula eget dolor.</p></div>
    <div><svg class="ic" style="width:9px;height:9px;stroke-width:1.2"><use href="#i-screen"/></svg><div class="h">Insert Text Here</div><p class="t">Lorem ipsum dolor sit amet, consectetuer adipiscing elit. Aenean commodo ligula eget dolor.</p></div>
    <div><svg class="ic" style="width:9px;height:9px;stroke-width:1.2"><use href="#i-bars"/></svg><div class="h">Insert Text Here</div><p class="t">Lorem ipsum dolor sit amet, consectetuer adipiscing elit. Aenean commodo ligula eget dolor.</p></div>
    <div><svg class="ic" style="width:9px;height:9px;stroke-width:1.2"><use href="#i-doc"/></svg><div class="h">Insert Text Here</div><p class="t">Lorem ipsum dolor sit amet, consectetuer adipiscing elit. Aenean commodo ligula eget dolor.</p></div>
    <div><svg class="ic" style="width:9px;height:9px;stroke-width:1.2"><use href="#i-mail"/></svg><div class="h">Insert Text Here</div><p class="t">Lorem ipsum dolor sit amet, consectetuer adipiscing elit. Aenean commodo ligula eget dolor.</p></div>
  </div>
  <div class="ft"><span class="pg">19</span>Copyright © 2017 Vane Crest | All Rights Reserved<span class="logo">VANE CREST</span></div>
</section>

<!-- 20 Diamonds -->
<section class="slide">
  <div class="hd">Vane Crest Powerpoint Template</div>
  <div class="abs row" style="left:10px;top:26px;width:202px;justify-content:space-between;text-align:center">
    <div style="width:44px"><div style="width:13px;height:13px;margin:2px auto 6px;border:0.8px solid var(--dark);border-radius:2px;transform:rotate(45deg);display:flex;align-items:center;justify-content:center;color:var(--red)"><svg class="ic" style="width:7px;height:7px;transform:rotate(-45deg)"><use href="#i-target"/></svg></div><div class="h">Title Text Demo</div><p class="t">Lorem ipsum dolor sit amet, consectetuer adipiscing elit. In it tortor in urna pulvinar blandit.</p></div>
    <div style="width:44px"><div style="width:13px;height:13px;margin:2px auto 6px;border:0.8px solid var(--dark);border-radius:2px;transform:rotate(45deg);display:flex;align-items:center;justify-content:center;color:var(--red)"><svg class="ic" style="width:7px;height:7px;transform:rotate(-45deg)"><use href="#i-pie"/></svg></div><div class="h">Title Text Demo</div><p class="t">Lorem ipsum dolor sit amet, consectetuer adipiscing elit. In it tortor in urna pulvinar blandit.</p></div>
    <div style="width:44px"><div style="width:13px;height:13px;margin:2px auto 6px;border:0.8px solid var(--dark);border-radius:2px;transform:rotate(45deg);display:flex;align-items:center;justify-content:center;color:var(--red)"><svg class="ic" style="width:7px;height:7px;transform:rotate(-45deg)"><use href="#i-clock"/></svg></div><div class="h">Title Text Demo</div><p class="t">Lorem ipsum dolor sit amet, consectetuer adipiscing elit. In it tortor in urna pulvinar blandit.</p></div>
    <div style="width:44px"><div style="width:13px;height:13px;margin:2px auto 6px;border:0.8px solid var(--dark);border-radius:2px;transform:rotate(45deg);display:flex;align-items:center;justify-content:center;color:var(--red)"><svg class="ic" style="width:7px;height:7px;transform:rotate(-45deg)"><use href="#i-doc"/></svg></div><div class="h">Title Text Demo</div><p class="t">Lorem ipsum dolor sit amet, consectetuer adipiscing elit. In it tortor in urna pulvinar blandit.</p></div>
  </div>
  <div class="abs" style="left:28px;right:28px;top:94px;height:10px;background:var(--red);border-radius:5px;display:flex;align-items:center;justify-content:center;font:700 4.2px Montserrat,sans-serif;color:#fff">Try a New Experience And Never Stop</div>
  <div class="ft"><span class="pg">20</span>Copyright © 2017 Vane Crest | All Rights Reserved<span class="logo">VANE CREST</span></div>
</section>

<!-- 21 Segmented ring -->
<section class="slide">
  <div class="hd">Vane Crest Powerpoint Template</div>
  <svg class="abs" style="left:81px;top:24px" width="60" height="60" viewBox="0 0 60 60">
    <g fill="#3a3a3a" stroke="#fff" stroke-width="1.4">
      <path d="M30 2 A28 28 0 0 1 54.2 16 L30 30Z"/><path d="M54.2 16 A28 28 0 0 1 54.2 44 L30 30Z" fill="#555"/>
      <path d="M54.2 44 A28 28 0 0 1 30 58 L30 30Z"/><path d="M30 58 A28 28 0 0 1 5.8 44 L30 30Z" fill="#555"/>
      <path d="M5.8 44 A28 28 0 0 1 5.8 16 L30 30Z"/><path d="M5.8 16 A28 28 0 0 1 30 2 L30 30Z" fill="#555"/>
    </g>
    <g fill="none" stroke="#fff" stroke-width="1"><circle cx="42" cy="12" r="2.5"/><circle cx="50" cy="30" r="2.5"/><circle cx="42" cy="48" r="2.5"/><circle cx="18" cy="48" r="2.5"/><circle cx="10" cy="30" r="2.5"/><circle cx="18" cy="12" r="2.5"/></g>
    <polygon points="30,16 42,23 42,37 30,44 18,37 18,23" fill="#ec1f27" stroke="#fff" stroke-width="1"/>
  </svg>
  <div class="abs logo" style="left:98px;top:52.5px;font-size:2.6px;color:#fff;letter-spacing:.1em">VANE CREST</div>
  <div class="abs" style="left:8px;top:20px;width:68px;text-align:right;display:flex;flex-direction:column;gap:9px">
    <div><div class="h red">Insert Text Here</div><p class="t">Lorem ipsum dolor sit amet, consectetuer adipiscing elit. Aenean commodo ligula.</p></div>
    <div><div class="h red">Insert Text Here</div><p class="t">Lorem ipsum dolor sit amet, consectetuer adipiscing elit. Aenean commodo ligula.</p></div>
    <div><div class="h red">Insert Text Here</div><p class="t">Lorem ipsum dolor sit amet, consectetuer adipiscing elit. Aenean commodo ligula.</p></div>
  </div>
  <div class="abs" style="left:146px;top:20px;width:68px;display:flex;flex-direction:column;gap:9px">
    <div><div class="h red">Insert Text Here</div><p class="t">Lorem ipsum dolor sit amet, consectetuer adipiscing elit. Aenean commodo ligula.</p></div>
    <div><div class="h red">Insert Text Here</div><p class="t">Lorem ipsum dolor sit amet, consectetuer adipiscing elit. Aenean commodo ligula.</p></div>
    <div><div class="h red">Insert Text Here</div><p class="t">Lorem ipsum dolor sit amet, consectetuer adipiscing elit. Aenean commodo ligula.</p></div>
  </div>
  <div class="ft"><span class="pg">21</span>Copyright © 2017 Vane Crest | All Rights Reserved<span class="logo">VANE CREST</span></div>
</section>

<!-- 22 Laptop mockup -->
<section class="slide">
  <div class="photo" style="left:0;top:0;width:222px;height:64px" role="img" aria-label="Dark photo of an office"></div>
  <div class="abs" style="left:10px;top:8px;width:84px;height:50px;background:linear-gradient(135deg,#f2f2f2,#bdbdbd);border-radius:2px" role="img" aria-label="Laptop mockup showing a bar chart"></div>
  <div class="abs" style="left:124px;top:14px;width:90px">
    <div class="title" style="font-size:5.2px;color:#fff;border-left:1.4px solid var(--red);padding-left:3px">Write Something About Your Title or Topic Here</div>
    <p class="t inv" style="margin-top:3px">Lorem ipsum dolor sit amet, consectetuer adipiscing elit. Aenean commodo ligula eget dolor. Aenean massa. Cum sociis natoque penatibus.</p>
  </div>
  <div class="abs row" style="left:8px;top:74px;width:206px;justify-content:space-between;text-align:center">
    <div style="width:44px"><div class="ring" style="width:11px;height:11px;margin:0 auto 3px"><svg class="ic" style="width:6px;height:6px"><use href="#i-target"/></svg></div><div class="h">Insert Text Here</div><p class="t">Lorem ipsum dolor sit amet, consectetuer</p></div>
    <div style="width:44px"><div class="ring" style="width:11px;height:11px;margin:0 auto 3px"><svg class="ic" style="width:6px;height:6px"><use href="#i-bars"/></svg></div><div class="h">Insert Text Here</div><p class="t">Lorem ipsum dolor sit amet, consectetuer</p></div>
    <div style="width:44px"><div class="ring" style="width:11px;height:11px;margin:0 auto 3px"><svg class="ic" style="width:6px;height:6px"><use href="#i-doc"/></svg></div><div class="h">Insert Text Here</div><p class="t">Lorem ipsum dolor sit amet, consectetuer</p></div>
    <div style="width:44px"><div class="ring" style="width:11px;height:11px;margin:0 auto 3px"><svg class="ic" style="width:6px;height:6px"><use href="#i-screen"/></svg></div><div class="h">Insert Text Here</div><p class="t">Lorem ipsum dolor sit amet, consectetuer</p></div>
  </div>
  <div class="ft"><span class="pg">22</span>Copyright © 2017 Vane Crest | All Rights Reserved<span class="logo">VANE CREST</span></div>
</section>

<!-- 23 Monitor mockup -->
<section class="slide">
  <div class="photo" style="left:0;top:0;width:222px;height:46px" role="img" aria-label="Dark photo of an office"></div>
  <div class="abs" style="left:12px;top:10px;width:90px;height:82px;background:linear-gradient(180deg,#f4f4f4,#bcbcbc);border-radius:2px" role="img" aria-label="Desktop monitor mockup showing a 68% donut chart"></div>
  <div class="abs" style="left:120px;top:14px;width:94px">
    <div class="h inv" style="font-size:4.2px;border-left:1.4px solid var(--red);padding-left:3px">Vane Crest Powerpoint</div>
    <p class="t inv" style="margin-top:2px">Lorem ipsum dolor sit amet, consectetuer adipiscing elit. Aenean commodo ligula eget dolor. Aenean massa.</p>
  </div>
  <div class="abs list" style="left:120px;top:54px;width:94px;gap:3px">
    <div class="item"><span class="dot dk"><svg class="ic"><use href="#i-bars"/></svg></span><div><div class="h">Insert Text Here</div><p class="t">Lorem ipsum dolor sit amet, consectetuer adipiscing elit.</p></div></div>
    <div class="item"><span class="dot dk"><svg class="ic"><use href="#i-pie"/></svg></span><div><div class="h">Insert Text Here</div><p class="t">Lorem ipsum dolor sit amet, consectetuer adipiscing elit.</p></div></div>
    <div class="item"><span class="dot dk"><svg class="ic"><use href="#i-clock"/></svg></span><div><div class="h">Insert Text Here</div><p class="t">Lorem ipsum dolor sit amet, consectetuer adipiscing elit.</p></div></div>
  </div>
  <div class="ft"><span class="pg">23</span>Copyright © 2017 Vane Crest | All Rights Reserved<span class="logo">VANE CREST</span></div>
</section>

<!-- 24 Tablet mockup -->
<section class="slide">
  <div class="photo" style="left:0;top:0;width:222px;height:60px" role="img" aria-label="Dark photo of city buildings"></div>
  <div class="abs" style="left:12px;top:6px;width:64px;height:104px;background:linear-gradient(180deg,#3a3a3a,#1e1e1e);border-radius:4px" role="img" aria-label="Tablet mockup showing a bar chart"></div>
  <div class="abs" style="left:100px;top:12px;width:114px">
    <div class="title" style="font-size:5.4px;color:#fff;border-left:1.4px solid var(--red);padding-left:3px">Write Something About Your Title or Topic Here</div>
    <p class="t inv" style="margin-top:3px">Lorem ipsum dolor sit amet, consectetuer adipiscing elit. Aenean commodo ligula eget dolor. Aenean massa. Cum sociis natoque penatibus.</p>
  </div>
  <div class="abs" style="left:100px;top:68px;width:114px;display:grid;grid-template-columns:1fr 1fr;gap:6px 6px">
    <div class="item"><span class="ring" style="width:7px;height:7px;flex:none"><svg class="ic" style="width:4px;height:4px"><use href="#i-bars"/></svg></span><div><div class="h">Insert Text Here</div><p class="t">Lorem ipsum dolor sit amet, consectetuer</p></div></div>
    <div class="item"><span class="ring" style="width:7px;height:7px;flex:none"><svg class="ic" style="width:4px;height:4px"><use href="#i-doc"/></svg></span><div><div class="h">Insert Text Here</div><p class="t">Lorem ipsum dolor sit amet, consectetuer</p></div></div>
    <div class="item"><span class="ring" style="width:7px;height:7px;flex:none"><svg class="ic" style="width:4px;height:4px"><use href="#i-screen"/></svg></span><div><div class="h">Insert Text Here</div><p class="t">Lorem ipsum dolor sit amet, consectetuer</p></div></div>
    <div class="item"><span class="ring" style="width:7px;height:7px;flex:none"><svg class="ic" style="width:4px;height:4px"><use href="#i-pie"/></svg></span><div><div class="h">Insert Text Here</div><p class="t">Lorem ipsum dolor sit amet, consectetuer</p></div></div>
  </div>
  <div class="ft"><span class="pg">24</span>Copyright © 2017 Vane Crest | All Rights Reserved<span class="logo">VANE CREST</span></div>
</section>

<!-- 25 Section break -->
<section class="slide dark">
  <div class="photo" style="inset:0;width:auto;height:auto;background:linear-gradient(135deg,#4a4c50,#232427)" role="img" aria-label="Dark photo of a city at dusk"></div>
  <div class="abs" style="left:0;right:0;top:42px;text-align:center">
    <div class="logo" style="font-size:6px;color:#fff">VANE CREST</div>
    <div class="title" style="font-size:11px;margin-top:2px">SECTION BREAK</div>
    <p class="t" style="width:190px;margin:5px auto 0">Lorem ipsum dolor sit amet, consectetuer adipiscing elit. Aenean commodo ligula eget dolor. Aenean massa. Cum sociis natoque penatibus et magnis dis parturient montes, nascetur ridiculus mus. Donec quam felis, ultricies nec, pellentesque eu, pretium quis, sem.</p>
  </div>
</section>

<!-- 26 Contact split -->
<section class="slide">
  <div class="abs" style="left:10px;top:14px;width:104px">
    <div class="title" style="font-size:7px;color:var(--dark)">CONTACT US</div>
    <p class="t" style="margin:3px 0 6px">Thank you for taking the time to go through this business profile. If there are any questions or comments, please feel free to contact us via any method listed below.</p>
    <div class="list" style="gap:5px">
      <div class="item" style="align-items:center"><span class="dot"><svg class="ic"><use href="#i-pin"/></svg></span><span class="t" style="color:var(--ink)"><b>Address</b> : Company Address</span></div>
      <div class="item" style="align-items:center"><span class="dot"><svg class="ic"><use href="#i-phone"/></svg></span><span class="t" style="color:var(--ink)"><b>Phone</b> : +12 555 010 200</span></div>
      <div class="item" style="align-items:center"><span class="dot"><svg class="ic"><use href="#i-mail"/></svg></span><span class="t" style="color:var(--ink)"><b>Email</b> : hello@vanecrest.com</span></div>
      <div class="item" style="align-items:center"><span class="dot"><svg class="ic"><use href="#i-globe"/></svg></span><span class="t" style="color:var(--ink)"><b>Website</b> : www.vanecrest.com</span></div>
    </div>
  </div>
  <div class="abs" style="left:120px;top:0;width:102px;height:125px;background:var(--dark);display:flex;align-items:center;justify-content:center">
    <span class="logo" style="font-size:6.5px;color:#fff;font-weight:500">VANE CREST</span>
  </div>
</section>

<!-- 27 Contact dark -->
<section class="slide dark">
  <div class="photo" style="inset:0;width:auto;height:auto;background:linear-gradient(180deg,#46484c,#242528)" role="img" aria-label="Dark photo of a city skyline"></div>
  <div class="abs" style="left:0;right:0;top:18px;text-align:center">
    <div class="title" style="font-size:7px">CONTACT US</div>
    <div class="logo" style="font-size:6px;color:#fff;margin-top:4px">VANE CREST</div>
    <p class="t" style="width:180px;margin:4px auto 0">Thank you for taking the time to go through this business profile. If there are any questions or comments, please feel free to contact us via any method listed below.</p>
  </div>
  <div class="abs row" style="left:14px;top:76px;width:194px;justify-content:space-between;text-align:center">
    <div style="width:44px"><span class="dot" style="width:9px;height:9px;margin:0 auto 3px"><svg class="ic" style="width:5px;height:5px"><use href="#i-pin"/></svg></span><div class="h inv">Address</div><p class="t">Company Address</p></div>
    <div style="width:44px"><span class="dot" style="width:9px;height:9px;margin:0 auto 3px"><svg class="ic" style="width:5px;height:5px"><use href="#i-phone"/></svg></span><div class="h inv">Phone</div><p class="t">+12 555 010 200</p></div>
    <div style="width:44px"><span class="dot" style="width:9px;height:9px;margin:0 auto 3px"><svg class="ic" style="width:5px;height:5px"><use href="#i-mail"/></svg></span><div class="h inv">Email</div><p class="t">hello@vanecrest.com</p></div>
    <div style="width:44px"><span class="dot" style="width:9px;height:9px;margin:0 auto 3px"><svg class="ic" style="width:5px;height:5px"><use href="#i-globe"/></svg></span><div class="h inv">Website</div><p class="t">www.vanecrest.com</p></div>
  </div>
</section>

</main>
</body>
</html>
```